Plakat-Design für Haushaltsreinigungen
Zielgruppe
Wir bieten haushaltsnahe Dienstleistungen für Privathaushalte an. Wir sind spezialisiert auf Haushaltsreinigungen für pflegebedürftige Personen.
Aufgabenstellung
Es geht darum dass auf dem Plakat zu erkennen ist, dass wir Haushaltsreinigungen anbieten die mit der Pflegekasse mit dem monatlichen Entlastungsbetrag von 125,- € abgerechnet werden können. Viele pflegebdürftige Personen ab einem Pflegegrad 1 wissen nicht, dass speziell für die Entlastungs im Alltag (Haushaltshilfen) ein monatliches Budget bei der Pflegekasse liegt und über zertifzierte Dienstleister wie wir es sind, abgerufen werden können. Somit lassen die pflegebdürftigen Personen dass Geld bei der Kasse verfallen.
Nun möcten wir mit der Plakatwerbung zum einen für unser Dienstleistungsunternehmen Werbung machen und Neukunden gewinnen, und zum anderen soll es auf den monatlichen Entlastungsbetrag hinweisen.
Folgende Slogans, haben wir mal auf die Schnelle uns ausgedacht, welche eventuell auf dem Plakat stehen könnten.
- Haushaltshilfe für Pflegebedürftige
- Lindmoor Haushaltshilfen Abrechnung direkt über alle Pflegekassen
- Keine Zuzahlung ab Pflegegrad 1
- Nutzen Sie Ihren Entlastungsbetrag
- Haushaltshilfe ohne versteckte Kosten da direkt über Pflegekasse
- 125 € für Haushaltshilfe ab Pflegegrad 1
- Neu in Esslingen
Auf dem Plakat soll neben der allgemeinen Botschaft natürlich auch unser Logo und unsere Kontaktdaten abgebildet sein.
Die Kontaktdaten lauten:
www.lindmoor.de
E-Mail: info@lindmoor.de
Tel.: 0711 83 27 60 95
Unten aufgeführt noch die technischen Daten für das Plakat:
Die Größe das Plakats beträgt 9 m²
Dateiformat: 590mm x 410mm (Maßstab 1:6)
kein Beschnitt, keine Beschnittzeichen
Sicherheitsabstand 2 cm zum Rand
Datenformat: PDF/X4
Auflösung: mind. 150dpi, CMYK

```html
<!DOCTYPE html>
<html lang="de">
<head>
<meta charset="utf-8">
<title>Lindmoor Haushaltshilfen – Plakat</title>
<link href="https://fonts.googleapis.com/css2?family=Cinzel:wght@400;600;700&family=Roboto+Condensed:wght@500;700&family=Open+Sans:wght@600&display=swap" rel="stylesheet">
<style>
  :root {
    --backdrop: #04316a;
    --red: #c0102c;
    --red-dark: #8e0d1f;
    --ink: #2b2b2b;
    --white: #ffffff;
    --grey-shadow: #b9bcc0;
  }
  html, body { margin: 0; padding: 0; overflow: hidden; }
  body {
    width: 1200px; height: 1200px;
    background: var(--backdrop);
    position: relative;
  }
  .poster {
    position: absolute; left: 41px; top: 237px;
    width: 1123px; height: 780px;
    background: var(--white);
    overflow: hidden;
  }
  .header { position: absolute; left: 0; top: 0; width: 100%; height: 110px; text-align: center; }
  .headline {
    margin: 0; padding-top: 14px;
    font: 700 44px/1 "Cinzel", serif;
    color: var(--ink); letter-spacing: 2px;
  }
  .ticker {
    margin: 14px 0 0;
    font: 400 21px/1 "Cinzel", serif;
    color: var(--red); letter-spacing: 1px; white-space: nowrap;
  }
  .ticker .plus { color: var(--ink); font-family: "Open Sans", sans-serif; font-size: 15px; }
  .photo {
    position: absolute; left: 0; top: 110px; width: 100%; height: 526px;
    background:
      radial-gradient(ellipse 320px 380px at 540px 260px, #6f9cc4 0%, rgba(111,156,196,0) 70%),
      linear-gradient(90deg, #e8ebee 0%, #cfd5da 35%, #b9cdd9 60%, #e5edf1 100%);
  }
  .badge {
    position: absolute; left: 43px; top: 219px; width: 294px; height: 294px;
    border-radius: 50%; overflow: hidden;
    border: 2px solid var(--red);
    box-sizing: border-box;
    background: linear-gradient(180deg, var(--white) 0 51%, var(--red) 51% 100%);
    text-align: center;
    font-family: "Roboto Condensed", sans-serif;
  }
  .badge-amount { margin: 32px 0 0; color: var(--red-dark); font-weight: 700; font-size: 22px; line-height: 1; }
  .badge-amount strong { font-size: 36px; }
  .badge-line { margin: 6px 0 0; color: var(--red-dark); font-weight: 700; font-size: 23px; line-height: 1; }
  .badge-grade { margin: 6px 0 0; color: var(--red-dark); font-weight: 700; font-size: 34px; line-height: 1; }
  .badge-call { margin: 20px 0 0; color: var(--white); font-weight: 700; font-size: 33px; line-height: 1; }
  .badge-phone { margin: 6px 0 0; color: var(--white); font-weight: 700; font-size: 29px; line-height: 1; letter-spacing: 1px; }
  .badge-icon { display: block; margin: 10px auto 0; }
  .bubble { position: absolute; left: 720px; top: 120px; }
  .bubble-text {
    position: absolute; left: 833px; top: 164px; width: 270px;
    text-align: center; margin: 0;
    font: 700 38px/1.22 "Roboto Condensed", sans-serif; color: var(--red);
  }
  .claim-strip {
    position: absolute; left: 0; top: 636px; width: 100%; height: 47px;
    background: var(--white);
  }
  .claim {
    margin: 0; padding: 9px 0 0 16px;
    font: 400 27px/1 "Cinzel", serif; color: var(--red); letter-spacing: 1.5px;
  }
  .claim b { color: var(--ink); font-weight: 700; }
  .contact-band {
    position: absolute; left: 0; top: 683px; width: 100%; height: 97px;
    background: linear-gradient(90deg, var(--red) 0%, var(--red) 55%, #d66a7a 72%, var(--white) 82%, var(--white) 100%);
  }
  .contact {
    position: absolute; top: 30px;
    display: flex; align-items: center; gap: 14px;
    font: 600 35px/1 "Open Sans", sans-serif; color: var(--white);
  }
  .contact.web { left: 29px; }
  .contact.mail { left: 424px; }
  .brand-mark {
    position: absolute; left: 898px; top: 546px;
    width: 146px; height: 146px; border-radius: 50%;
    border: 8px solid var(--red); box-sizing: border-box;
    background: var(--white);
  }
  .brand-name {
    position: absolute; left: 840px; top: 701px; width: 270px; margin: 0;
    text-align: center;
    font: 600 42px/1 "Cinzel", serif; color: var(--ink); letter-spacing: 1px;
  }
</style>
</head>
<body>
  <main class="poster">
    <header class="header">
      <h1 class="headline">Haushaltshilfe für Pflegebedürftige</h1>
      <p class="ticker">Neu in Esslingen <span class="plus">+++</span> Neu in Esslingen <span class="plus">+++</span> Neu in Esslingen <span class="plus">+++</span> Neu in Esslingen <span class="plus">+++</span></p>
    </header>

    <div class="photo" role="img" aria-label="Foto: lächelnde Haushaltshilfe im blauen Shirt putzt ein Fenster mit Sprühflasche und rotem Tuch"></div>

    <div class="badge">
      <p class="badge-amount">mind.<strong>125 €</strong> mt.</p>
      <p class="badge-line">für Haushaltshilfe ab</p>
      <p class="badge-grade">Pflegegrad 1</p>
      <p class="badge-call">Gleich anrufen!</p>
      <p class="badge-phone">0711 83 27 60 95</p>
      <svg class="badge-icon" width="40" height="40" viewBox="0 0 40 40" aria-hidden="true">
        <rect width="40" height="40" rx="6" fill="#ffffff"/>
        <path d="M13 10c1-1 2.5-1 3.2.2l2 3.2c.6 1 .3 2.1-.5 2.8l-1.3 1c.9 2 2.5 3.7 4.5 4.6l1-1.3c.7-.8 1.9-1.1 2.8-.5l3.2 2c1.2.7 1.2 2.2.2 3.2l-1.5 1.5c-1.3 1.3-3.3 1.6-5 .8-4.7-2.2-8.4-5.9-10.6-10.6-.8-1.7-.5-3.7.8-5z" fill="#c0102c"/>
      </svg>
    </div>

    <svg class="bubble" width="400" height="320" viewBox="0 0 400 320" aria-hidden="true">
      <g fill="#b9bcc0" transform="translate(7 8)">
        <path d="M125 178 L19 199 Q110 232 172 266 Z"/>
        <circle cx="248" cy="156" r="136"/>
      </g>
      <g fill="#ffffff">
        <path d="M125 178 L19 199 Q110 232 172 266 Z"/>
        <circle cx="248" cy="156" r="136"/>
      </g>
    </svg>
    <p class="bubble-text">Nutzen<br>Sie Ihren<br>Entlastungs-<br>betrag!</p>

    <div class="claim-strip">
      <p class="claim">Abrechnung mit <b>allen</b> Pflegekassen möglich</p>
    </div>

    <footer class="contact-band">
      <div class="contact web">
        <svg width="34" height="34" viewBox="0 0 34 34" aria-hidden="true">
          <rect width="34" height="34" rx="5" fill="#ffffff"/>
          <g fill="none" stroke="#c0102c" stroke-width="1.8">
            <circle cx="17" cy="17" r="10"/>
            <ellipse cx="17" cy="17" rx="4.5" ry="10"/>
            <path d="M7 17h20M9 12h16M9 22h16"/>
          </g>
        </svg>
        <span>www.lindmoor.de</span>
      </div>
      <div class="contact mail">
        <svg width="34" height="34" viewBox="0 0 34 34" aria-hidden="true">
          <rect width="34" height="34" rx="5" fill="#ffffff"/>
          <g fill="none" stroke="#c0102c" stroke-width="2">
            <rect x="7" y="10" width="20" height="14"/>
            <path d="M7 10l10 8 10-8M7 24l7-7M27 24l-7-7"/>
          </g>
        </svg>
        <span>info@lindmoor.de</span>
      </div>
    </footer>

    <div class="brand-mark" aria-hidden="true"></div>
    <p class="brand-name">Lindmoor</p>
  </main>
</body>
</html>
```